Nineteen Musts and Nevers for Property Lending or the 22 things that will derail your transaction and how to prevent them.

I am looking to do a series of 4 to 5 e-books that should have a consistent format and theme

The first of these should be entitled, "Nineteen Musts and Nevers for Property Lending" That is similar in style to the attached e-book.
The attached e-book is pretty much the style that I am looking for, The same format can be followed. I have attached a black and white head shot image for the head shot areas that appears on page two of the attached e-book. I have also attached my company logo.
Please feel free to use the same or similar colors in my logo for the lay-out of the e-book. However please do not feel limited to those colors. - Feel free to use your imagination.

The content can be found here.

http://www.glenthecashguy.com/loan-advice.php

For the final “About” page of the e-book - Please entitle it… About Glen the Cash Guy.
The content for the last page can be found in the attached document - Glen Hartwell bio2

The first page is where the creativity come in

Requirements
Must have
• Note that this project is for one e-book - However, once the designer and format is chosen the remainder of the projects will be launched

```html
<!DOCTYPE html>
<html lang="en">
<head>
<meta charset="utf-8">
<title>Nineteen Musts and Nevers for Property Lending – Page 9</title>
<link href="https://fonts.googleapis.com/css2?family=Jost:wght@300;400;500;600&family=Playfair+Display:wght@700&family=Cormorant+SC:wght@600;700&display=swap" rel="stylesheet">
<style>
  :root {
    --navy: #1f3769;
    --do-blue: #2c5ea6;
    --dont-red: #d6282b;
    --body-ink: #3a3a3a;
    --callout: #3b66ad;
    --paper: #ffffff;
  }
  * { box-sizing: border-box; margin: 0; padding: 0; }
  html, body { width: 900px; height: 1200px; overflow: hidden; background: var(--paper); }
  .page { position: relative; width: 900px; height: 1200px; font-family: "Jost", sans-serif; color: var(--body-ink); }

  .tip { position: absolute; left: 64px; width: 772px; }
  .tip-number {
    position: absolute; left: -46px; top: -4px;
    width: 50px; height: 50px; border-radius: 50%;
    background: var(--navy); color: #fff;
    font-family: "Playfair Display", serif; font-weight: 700; font-size: 25px;
    display: flex; align-items: center; justify-content: center;
  }
  .tip-heading {
    font-weight: 500; font-size: 29px; line-height: 36px; color: var(--navy);
    text-indent: 42px; margin-bottom: 14px; letter-spacing: 0.1px;
  }
  .tip-heading .do { color: var(--do-blue); font-weight: 600; }
  .tip-heading .dont { color: var(--dont-red); font-weight: 600; }
  .tip-body { font-weight: 300; font-size: 15.5px; line-height: 23px; color: var(--body-ink); }

  .tip-19 { top: 55px; }
  .tip-20 { top: 274px; }
  .tip-21 { top: 500px; }
  .tip-22 { top: 729px; }

  .callout {
    position: absolute; left: 64px; top: 928px; width: 760px;
    font-weight: 600; font-size: 17.5px; line-height: 29px; color: var(--callout);
  }

  .footer {
    position: absolute; left: 64px; right: 64px; top: 1098px; height: 44px;
    display: flex; align-items: center;
  }
  .brand { display: flex; align-items: center; gap: 7px; width: 116px; }
  .brand-mark { width: 12px; height: 12px; background: var(--navy); }
  .brand-name { font-family: "Jost", sans-serif; font-weight: 600; font-size: 12px; line-height: 13px; color: var(--navy); }
  .footer-rule { width: 2px; height: 36px; background: var(--navy); margin: 0 10px 0 8px; }
  .footer-title, .footer-licence {
    font-family: "Cormorant SC", serif; font-weight: 700; font-size: 16px; color: var(--navy); letter-spacing: 0.3px;
  }
  .footer-title { width: 380px; }
  .footer-licence { flex: 1; }
  .page-number {
    width: 28px; height: 28px; background: var(--navy); color: #fff;
    font-family: "Cormorant SC", serif; font-weight: 700; font-size: 17px;
    display: flex; align-items: center; justify-content: center;
  }
</style>
</head>
<body>
<main class="page">

  <section class="tip tip-19">
    <div class="tip-number">19</div>
    <h2 class="tip-heading"><span class="do">Do</span> inform your mortgage professional of any private notes, loans, or debts that do not appear on your credit report.</h2>
    <p class="tip-body">As with the previous “do,” if your loan approval is at the edge of the lenders al-lowable debt-to-income ratio, the extra monthly payments on the undisclosed debt could effect your debt-to-income ratio in a similar manner to the previous example, resulting in a loan denial.</p>
  </section>

  <section class="tip tip-20">
    <div class="tip-number">20</div>
    <h2 class="tip-heading"><span class="dont">Don’t</span> change your name legally with the courts or file for divorce during the un-derwriting process.</h2>
    <p class="tip-body">It is not often that someone takes the time to change their name or file for di-vorce during the underwriting process but, it has been known to happen any changes to a borrower’s legal name or marriage status during the underwriting process will delay closing. When in doubt contact your realtor or mortgage pro-fessional before making any changes to your name, marriage status or residen-cy during the underwriting process.</p>
  </section>

  <section class="tip tip-21">
    <div class="tip-number">21</div>
    <h2 class="tip-heading"><span class="dont">Don’t</span> close any bank accounts during the underwriting process.</h2>
    <p class="tip-body">If you have consolidated funds for your downpayment, closing costs and prepaid items from multiple bank accounts into one single account for convenience. Please do not close the accounts those funds came out of even if this leaves any account with a zero balance. The lender will want to see what accounts the consolidated accounts came from and if you close an account those funds can’t be traced back to the closed account.</p>
  </section>

  <section class="tip tip-22">
    <div class="tip-number">22</div>
    <h2 class="tip-heading"><span class="dont">Don’t</span> put a credit freeze on your social security number during the underwriting process.</h2>
    <p class="tip-body">In an age where hackers can gain access even to the national tax agency’s database of social security numbers there is a temptation to freeze access to your credit data at the bureau or repository level as a precaution. A credit refresh may be required by either your mortgage broker or the final lender prior to closing your loan. If you have placed a credit freeze on your social security number no credit refresh can be done as Creditora, Verilo and Tallyline will reject any request for new credit data.</p>
  </section>

  <p class="callout">While this will not prevent your loan from closing it will belay the processing of your loan unnecessarily.</p>

  <footer class="footer">
    <div class="brand">
      <span class="brand-mark"></span>
      <span class="brand-name">Cascade Harbor Lending</span>
    </div>
    <span class="footer-rule"></span>
    <span class="footer-title">Nineteen Musts and Nevers for Property Lending</span>
    <span class="footer-licence">Licence MLO#40728</span>
    <span class="page-number">9</span>
  </footer>

</main>
</body>
</html>
```